Business Card design

We have found an idea we would like to do something similar.
We would require the cards for the inside and the wrapping sheet for the outside, you will see what I mean when you see the image attached. (gum packet) The company is called.... Tallowmere Swift Press
I will include the company logo also.
If you could create the outside wrapping with the ability to have staff members name and mobile, maybe on one side panel we would have the address, the other side would be phone numbers, the front would be staff members name and mobile number and email. The other side would be company name and logo if it fits, the logo could wrap around if needed. Open to all ideas.

```html
<!DOCTYPE html>
<html lang="en">
<head>
<meta charset="utf-8">
<title>Tallowmere Swift Press – Business Card</title>
<link href="https://fonts.googleapis.com/css2?family=Arimo:wght@400;700&display=swap" rel="stylesheet">
<style>
  :root {
    --backdrop: #a0a09e;
    --paper: #ffffff;
    --gold: #e4a823;
    --orange: #df8a26;
    --red: #d24b27;
    --ink: #111111;
    --ink-soft: #3a3a3a;
  }
  * { box-sizing: border-box; margin: 0; padding: 0; }
  html, body { width: 1200px; height: 1200px; overflow: hidden; }
  body {
    background: var(--backdrop);
    font-family: "Arimo", Arial, sans-serif;
    color: var(--ink);
    position: relative;
  }
  .card {
    position: absolute;
    left: 94px;
    width: 1012px;
    height: 290px;
    background: var(--paper);
    box-shadow: 0 2px 3px rgba(0,0,0,.25);
    overflow: hidden;
  }
  .card--front { top: 279px; }
  .card--back { top: 634px; }

  .wave { position: absolute; inset: 0; width: 100%; height: 100%; }

  .brand-mini {
    position: absolute;
    left: 38px;
    top: 26px;
    width: 140px;
    text-align: center;
  }
  .brand-mini .mark {
    width: 96px; height: 96px;
    border-radius: 50%;
    background: var(--orange);
    margin: 0 auto 14px;
  }
  .brand-mini .name {
    font-size: 19px;
    line-height: 1.2;
    color: var(--ink-soft);
  }

  .person {
    position: absolute;
    right: 62px;
    top: 30px;
    text-align: right;
  }
  .person .name {
    font-weight: 700;
    font-size: 34px;
    color: var(--gold);
    line-height: 1.1;
  }
  .person .role {
    font-size: 26px;
    line-height: 1.3;
  }

  .contacts {
    position: absolute;
    right: 62px;
    top: 160px;
    list-style: none;
    text-align: right;
  }
  .contacts li {
    font-size: 26px;
    line-height: 32px;
    display: flex;
    justify-content: flex-end;
    align-items: center;
    gap: 14px;
  }
  .contacts svg { width: 22px; height: 22px; fill: var(--ink); }

  .brand-lockup {
    position: absolute;
    left: 0; right: 0;
    top: 58px;
    display: flex;
    justify-content: center;
    align-items: center;
    gap: 28px;
  }
  .brand-lockup .mark {
    width: 140px; height: 140px;
    border-radius: 50%;
    background: var(--orange);
    flex: none;
  }
  .brand-lockup .name {
    font-size: 50px;
    line-height: 1.15;
    color: var(--ink-soft);
    width: 380px;
  }
  .address {
    position: absolute;
    left: 0; right: 54px;
    top: 226px;
    text-align: center;
    font-size: 26px;
  }
</style>
</head>
<body>

<section class="card card--front">
  <svg class="wave" viewBox="0 0 1012 290" preserveAspectRatio="none" aria-hidden="true">
    <path fill="var(--gold)" d="M0,262 C250,285 500,240 700,170 C820,130 920,112 1012,134 L1012,290 L0,290 Z"/>
    <path fill="var(--orange)" d="M0,229 C200,268 420,250 562,200 C420,256 220,280 0,258 Z"/>
    <path fill="var(--red)" d="M150,245 C400,250 600,190 760,140 C860,110 950,106 1012,112 L1012,126 C940,120 860,128 760,156 C600,206 400,252 150,245 Z"/>
  </svg>

  <div class="brand-mini">
    <div class="mark"></div>
    <div class="name">Tallowmere Swift Press</div>
  </div>

  <div class="person">
    <div class="name">Marcus Ellery</div>
    <div class="role">Manager</div>
  </div>

  <ul class="contacts">
    <li>123-456-2100
      <svg viewBox="0 0 24 24"><path d="M6.6 10.8a15 15 0 0 0 6.6 6.6l2.2-2.2c.3-.3.7-.4 1-.2 1.1.4 2.3.6 3.6.6.6 0 1 .4 1 1V20c0 .6-.4 1-1 1A17 17 0 0 1 3 4c0-.6.4-1 1-1h3.5c.6 0 1 .4 1 1 0 1.3.2 2.5.6 3.6.1.3 0 .7-.2 1z"/></svg>
    </li>
    <li>youremail@mailbox.com
      <svg viewBox="0 0 24 24"><path d="M2 5h20v14H2z M2 5l10 8 10-8" stroke="#fff" stroke-width="1.6"/></svg>
    </li>
    <li>www.yourwebsite.com
      <svg viewBox="0 0 24 24"><circle cx="12" cy="12" r="10"/><path d="M2 12h20M12 2c3 3 3 17 0 20M12 2c-3 3-3 17 0 20" stroke="#fff" stroke-width="1.4" fill="none"/></svg>
    </li>
  </ul>
</section>

<section class="card card--back">
  <div class="brand-lockup">
    <div class="mark"></div>
    <div class="name">Tallowmere Swift Press</div>
  </div>
  <p class="address">Your address, city, state, ZIP 0000</p>
</section>

</body>
</html>
```